Modern wordpress-enabled design wanted for translations agency serving large corporations

We are a translation agency and we only work for corporate clients and not private individuals. We are currently using the Larvesk wordpress theme and an upload feature called trobanex. It is important that prospective clients can upload their file. So we need a cool design for that kind of feature. We offer different kinds of translations tailored to the needs or global corporations. Corporate communications translations, legal translations, financial translations, healthcare translations, financial translations, audit translations.

```html
<!DOCTYPE html>
<html lang="en">
<head>
<meta charset="utf-8">
<title>Translation Agency</title>
<link href="https://fonts.googleapis.com/css2?family=Open+Sans:wght@400;600;700&display=swap" rel="stylesheet">
<style>
:root{
  --green:#8cc63f;
  --green-dark:#6fa82a;
  --blue:#2ea3dd;
  --blue-dark:#1f86bd;
  --blue-light:#5bb8e6;
  --text:#4a4a4a;
  --muted:#8a8a8a;
  --line:#e3e3e3;
  --footer:#eef2e6;
  --white:#fff;
}
*{margin:0;padding:0;box-sizing:border-box}
html,body{width:732px;height:1200px;overflow:hidden;background:var(--white)}
body{font-family:"Open Sans",Arial,sans-serif;color:var(--text);font-size:7px;line-height:1.45}
.wrap{width:652px;margin:0 auto;position:relative}
h2,h3{font-weight:600}
.btn{display:inline-block;background:var(--green);color:var(--white);font-size:6.5px;font-weight:700;padding:4px 10px;border-radius:2px;text-transform:uppercase}
.btn.light{background:var(--blue-dark)}

/* header */
.site-header{height:58px;display:flex;justify-content:space-between;align-items:center}
.brand{display:flex;align-items:center;gap:7px}
.brand-mark{width:26px;height:26px;border-radius:50%;background:var(--green)}
.brand-name{font-size:17px;font-weight:600;color:var(--green-dark);line-height:1}
.header-right{text-align:right}
.social{display:flex;gap:4px;justify-content:flex-end;margin-bottom:5px}
.social span{width:11px;height:11px;background:var(--muted);border-radius:2px}
.call{font-size:9px;font-weight:700;color:var(--text)}
.call b{color:var(--blue)}

/* nav */
.main-nav{height:24px;background:var(--green);border-radius:3px;display:flex}
.main-nav a{flex:1;text-align:center;color:var(--white);font-size:7.5px;font-weight:600;line-height:24px;text-decoration:none;text-transform:uppercase}
.main-nav a.active{background:var(--green-dark)}

/* about */
.about{display:flex;gap:14px;padding:14px 0 16px;height:242px}
.about-photo{width:118px;height:110px;background:linear-gradient(135deg,#d7c3ae,#a9c9e2);flex:none}
.about-body{flex:1}
.about-body h2{font-size:15px;color:var(--text);margin-bottom:5px}
.about-body p{margin-bottom:6px;color:var(--muted)}
.sidebar{width:160px;flex:none;background:var(--blue);padding:8px 10px;color:var(--white);height:175px}
.sidebar h3{font-size:8px;text-transform:uppercase;margin-bottom:6px}
.sidebar li{list-style:none;background:var(--white);color:var(--blue-dark);font-size:6.5px;font-weight:600;text-transform:uppercase;padding:3px 6px;margin-bottom:4px;display:flex;gap:5px;align-items:center}
.sidebar li::before{content:"";width:4px;height:4px;border-radius:50%;background:var(--green)}

/* services band */
.services-band{background:var(--blue);height:232px;padding:22px 0}
.services-band .wrap{display:flex;gap:24px}
.service{flex:1;color:var(--white)}
.service h2{font-size:15px;margin-bottom:6px}
.service p{margin-bottom:6px;color:#e6f4fb}
.service ul{list-style:none;margin-bottom:8px}
.service li{display:flex;align-items:center;gap:5px;margin-bottom:3px;font-weight:600}
.service li svg{flex:none}
.service.highlight{background:var(--blue-light);padding:8px 12px;flex:0 0 270px}

/* tabs */
.tabs{padding:16px 0 10px;height:124px}
.tab-list{display:flex;border-bottom:1px solid var(--line);margin-bottom:8px}
.tab-list span{font-size:8px;padding:4px 16px;color:var(--muted);border:1px solid transparent;border-bottom:none}
.tab-list span.active{color:var(--blue);border-color:var(--line);background:var(--white);margin-bottom:-1px;font-weight:600}
.tabs p{color:var(--muted)}

/* info columns */
.info{display:flex;gap:22px;padding:8px 0;height:118px;border-top:1px solid var(--line)}
.info-col{flex:1}
.info-col h3{font-size:13px;color:var(--blue);margin-bottom:5px}
.info-col p,.info-col li{color:var(--muted)}
.info-col ul{list-style:none}
.info-col li{display:flex;gap:5px;align-items:center;margin-bottom:3px}
.info-col li::before{content:"";width:4px;height:4px;border-radius:50%;background:var(--green)}
.quote{background:#f3f3f3;padding:6px 8px;font-style:italic}
.quote cite{display:block;font-style:normal;font-weight:600;color:var(--text);margin-top:4px}

/* team */
.team{text-align:center;padding:10px 0;height:180px}
.team h2{font-size:16px;color:var(--text);margin-bottom:12px}
.members{display:flex;justify-content:space-around}
.member{width:120px}
.member-photo{width:82px;height:82px;border-radius:50%;margin:0 auto 6px;border:3px solid var(--line);background:linear-gradient(160deg,#e8d6c6,#9fb4c6)}
.member-name{font-size:7.5px;font-weight:700;text-transform:uppercase;color:var(--text)}
.member-role{color:var(--muted);font-style:italic}

/* footer */
.site-footer{background:var(--footer);height:180px;position:relative}
.site-footer .wrap{display:flex;padding-top:16px;gap:10px}
.footer-col{flex:1;list-style:none}
.footer-col li{display:flex;gap:5px;align-items:center;margin-bottom:5px;font-size:6.5px;text-transform:uppercase;color:var(--text)}
.footer-col li::before{content:"";width:4px;height:4px;border-radius:50%;background:var(--green)}
.footer-brand{flex:0 0 110px;text-align:center}
.footer-brand .brand-mark{margin:0 auto 8px;width:30px;height:30px}
.footer-brand .social{justify-content:center}
.copyright{position:absolute;left:0;right:0;bottom:0;height:22px;background:var(--green-dark);color:var(--white);text-align:center;line-height:22px;font-size:6.5px}
</style>
</head>
<body>
<div class="wrap">
  <header class="site-header">
    <div class="brand"><span class="brand-mark"></span><span class="brand-name">Translation Agency</span></div>
    <div class="header-right">
      <div class="social"><span></span><span></span><span></span><span></span></div>
      <div class="call">CALL US NOW: <b>0123-555-0198</b></div>
    </div>
  </header>
  <nav class="main-nav">
    <a>Home</a><a class="active">About us</a><a>Language</a><a>Services</a><a>Contact us</a>
  </nav>

  <section class="about">
    <div class="about-photo" role="img" aria-label="Photo of a smiling business woman at a desk"></div>
    <div class="about-body">
      <h2>Our History</h2>
      <p>We translate documents for global corporations with care, precision and speed. Our certified linguists cover more than forty languages and every major business field, from finance to law and healthcare.</p>
      <p>Every project is managed by a dedicated coordinator who checks terminology, formatting and deadlines, so your teams receive files that are ready to publish.</p>
      <p>Clients upload files securely and receive a quote within one business day.</p>
      <span class="btn">Read more</span>
    </div>
    <aside class="sidebar">
      <h3>We translate:</h3>
      <ul>
        <li>Annual reports</li>
        <li>Financial statements</li>
        <li>Audit reports</li>
        <li>Legal contracts</li>
        <li>Health reports</li>
        <li>Others</li>
      </ul>
    </aside>
  </section>
</div>

<section class="services-band">
  <div class="wrap">
    <div class="service">
      <h2>Financial Translations</h2>
      <p>Financial translations demand exact figures and consistent terms. Our finance specialists handle annual reports, balance sheets, prospectuses and investor communications for listed companies across Europe, Asia and the Americas.</p>
      <ul>
        <li><svg width="7" height="7" viewBox="0 0 10 10"><circle cx="5" cy="5" r="5" fill="#fff"/><path d="M3 5l1.5 1.5L7 3.5" stroke="#2ea3dd" stroke-width="1.4" fill="none"/></svg>Annual and quarterly financial reports</li>
        <li><svg width="7" height="7" viewBox="0 0 10 10"><circle cx="5" cy="5" r="5" fill="#fff"/><path d="M3 5l1.5 1.5L7 3.5" stroke="#2ea3dd" stroke-width="1.4" fill="none"/></svg>Audit reports and accounting statements</li>
        <li><svg width="7" height="7" viewBox="0 0 10 10"><circle cx="5" cy="5" r="5" fill="#fff"/><path d="M3 5l1.5 1.5L7 3.5" stroke="#2ea3dd" stroke-width="1.4" fill="none"/></svg>Prospectuses and investor presentations</li>
      </ul>
      <span class="btn light">View more</span>
    </div>
    <div class="service highlight">
      <h2>Health</h2>
      <p>Medical and pharmaceutical texts are translated by qualified healthcare linguists who know the regulations of each market.</p>
      <ul>
        <li><svg width="7" height="7" viewBox="0 0 10 10"><circle cx="5" cy="5" r="5" fill="#fff"/><path d="M3 5l1.5 1.5L7 3.5" stroke="#5bb8e6" stroke-width="1.4" fill="none"/></svg>Clinical trial documents</li>
        <li><svg width="7" height="7" viewBox="0 0 10 10"><circle cx="5" cy="5" r="5" fill="#fff"/><path d="M3 5l1.5 1.5L7 3.5" stroke="#5bb8e6" stroke-width="1.4" fill="none"/></svg>Patient information leaflets</li>
        <li><svg width="7" height="7" viewBox="0 0 10 10"><circle cx="5" cy="5" r="5" fill="#fff"/><path d="M3 5l1.5 1.5L7 3.5" stroke="#5bb8e6" stroke-width="1.4" fill="none"/></svg>Medical device manuals</li>
      </ul>
      <span class="btn light">View more</span>
    </div>
  </div>
</section>

<div class="wrap">
  <section class="tabs">
    <div class="tab-list"><span class="active">Translations</span><span>Resources</span><span>Other services</span></div>
    <p>Our translation team works with corporate communications, legal contracts, financial statements, healthcare documentation and audit reports. Each text is translated by a native speaker, reviewed by a second linguist and checked for consistent terminology before delivery. We use secure file transfer and strict confidentiality agreements for every client, and we adapt our workflow to your internal review processes and publishing systems.</p>
  </section>

  <section class="info">
    <div class="info-col">
      <h3>Who we are?</h3>
      <p>We are a team of professional linguists, project managers and subject experts serving large corporations since 2004.</p>
    </div>
    <div class="info-col">
      <h3>Why Us?</h3>
      <ul>
        <li>Native speaking translators</li>
        <li>Fast turnaround</li>
        <li>Secure upload of your files</li>
        <li>Certified quality process</li>
      </ul>
    </div>
    <div class="info-col">
      <h3>Client's Testimonial</h3>
      <div class="quote">"Precise translations delivered on time, every time. Their team made our annual report launch in six languages effortless."<cite>Helena Brant, Communications Director</cite></div>
    </div>
  </section>

  <section class="team">
    <h2>Meet our Team</h2>
    <div class="members">
      <div class="member"><div class="member-photo" role="img" aria-label="Portrait of a team member"></div><div class="member-name">Mara Ellison</div><div class="member-role">Manager</div></div>
      <div class="member"><div class="member-photo" role="img" aria-label="Portrait of a team member"></div><div class="member-name">Lena Varga</div><div class="member-role">Project Manager</div></div>
      <div class="member"><div class="member-photo" role="img" aria-label="Portrait of a team member"></div><div class="member-name">Owen Castell</div><div class="member-role">Sr. Project Manager</div></div>
      <div class="member"><div class="member-photo" role="img" aria-label="Portrait of a team member"></div><div class="member-name">Tessa Wynne</div><div class="member-role">Marketing</div></div>
    </div>
  </section>
</div>

<footer class="site-footer">
  <div class="wrap">
    <ul class="footer-col"><li>Home</li><li>About us</li><li>Services</li><li>Solutions</li></ul>
    <ul class="footer-col"><li>News</li><li>Careers</li><li>Policy</li><li>Terms &amp; conditions</li></ul>
    <ul class="footer-col"><li>Jobs</li><li>Languages</li><li>Our experts</li><li>Newsletters</li></ul>
    <ul class="footer-col"><li>Case studies</li><li>Extra services</li><li>FAQ</li><li>Urgent translation</li></ul>
    <div class="footer-brand">
      <div class="brand-mark"></div>
      <div class="social"><span></span><span></span><span></span><span></span></div>
    </div>
  </div>
  <div class="copyright">© 2024 Translation Agency. All rights reserved.</div>
</footer>
</body>
</html>
```